New, modern business card for growing audiology practice

We need a new business card for our audiology practice. Our logo and website have recently changed (more modern) and we want our business cards to reflect this change.
We conduct hearing tests, perform earwax removals, and fit & dispense hearing aids to our patients. We are a family owned practice in which the owner is the one who works directly with the patient. I have attached logos in various formats to use, as well as two ideas I found on this website; as well as a scanned copy of our current logo. Good luck!

Industry/Entity Type

Business

Contact Information for Business Card

Company name: Maplow Hearing Center
Provider name: Peter Mulvoy, Au.D. F/ISN
Phone number: (555) 318-6042
Address: 87 W. Linden Ave. Brookmere, OH 45190
email: maplowhearing@postvale.net
website: maplowhearing.com

Colors
000000
aaaaaa
dbdbdb
cacaca
9bcb3c
afd23c
cadf82
b1b1b1

Requirements
Must have
• My card must include information in the "details" section. In the attached images, I found a few that I liked and I would like to model after - "brisk tumblin'" and "Sound Wellness Center".
• Must be horizontal.
• Must include logos provided. I uploaded them in various file formats and various ways.
• Must match logo font, if possible, if not, please get as close as you can.
Nice to have
• I really like the idea of having a color on one side with just the logo and company name and the contact information and provider name on the other side. I also really like the idea of having the main color dominating on the logo/company side with accent of that same color on the contact side of the card.
Should not have
• Must not be vertical.

```html
<!DOCTYPE html>
<html lang="en">
<head>
<meta charset="utf-8">
<title>Maplow Hearing Center – Business Card</title>
<link rel="stylesheet" href="https://fonts.googleapis.com/css2?family=Quicksand:wght@400;500;600&display=swap">
<style>
  :root {
    --stage: #111111;
    --green: #9bcb3c;
    --green-mid: #afd23c;
    --green-light: #cadf82;
    --charcoal: #33373a;
    --ink: #1a1a1a;
    --white: #ffffff;
    --grey-text: #dbdbdb;
    --grey-soft: #cacaca;
  }
  * { box-sizing: border-box; margin: 0; padding: 0; }
  html, body { width: 1200px; height: 1000px; overflow: hidden; }
  body {
    background: var(--stage);
    font-family: "Quicksand", "Century Gothic", sans-serif;
    position: relative;
  }
  .card {
    position: absolute;
    width: 540px;
    height: 310px;
    border-radius: 22px;
    overflow: hidden;
  }

  /* ---------- Brand side ---------- */
  .card--brand {
    left: 40px; top: 345px;
    background: radial-gradient(ellipse at 45% 42%, var(--green-light) 0%, var(--green-mid) 45%, var(--green) 100%);
  }
  .brand-name {
    position: absolute;
    left: 70px; top: 136px;
    display: flex; align-items: center; gap: 10px;
    font-weight: 600;
    font-size: 25px;
    letter-spacing: 0.5px;
    color: var(--ink);
    text-transform: uppercase;
    white-space: nowrap;
  }
  .brand-dot {
    width: 14px; height: 14px; border-radius: 50%;
    background: var(--ink);
    flex: none;
  }

  /* ---------- Contact side ---------- */
  .card--contact {
    left: 620px; top: 345px;
    background: var(--charcoal);
  }
  .contact-top {
    position: absolute; left: 0; top: 0; right: 0; height: 118px;
    background: var(--white);
  }
  .contact-logo {
    position: absolute; right: 28px; top: 72px;
    display: flex; align-items: center; gap: 10px;
    font-weight: 600; font-size: 23px; letter-spacing: 0.4px;
    color: var(--charcoal); text-transform: uppercase;
    white-space: nowrap;
  }
  .contact-logo .brand-dot {
    width: 40px; height: 40px;
    background: var(--white);
    border: 5px solid var(--green);
  }
  .provider {
    position: absolute; left: 30px; top: 134px;
    font-weight: 600; font-size: 17px; color: var(--green);
    white-space: nowrap;
  }
  .details {
    position: absolute; left: 30px; top: 166px;
    list-style: none;
    font-size: 13px; color: var(--grey-text);
    line-height: 21px;
  }
  .details li { display: flex; align-items: center; gap: 8px; white-space: nowrap; }
  .details svg { width: 11px; height: 11px; fill: var(--green); flex: none; }
  .details .accent { color: var(--green); }
  .address {
    position: absolute; right: 30px; top: 180px;
    text-align: right; font-style: normal;
    font-size: 14px; line-height: 19px; color: var(--grey-soft);
    white-space: nowrap;
  }
  .contact-stripe {
    position: absolute; left: 0; right: 0; bottom: 38px; height: 6px;
    background: var(--white);
  }
  .contact-band {
    position: absolute; left: 0; right: 0; bottom: 0; height: 38px;
    background: linear-gradient(90deg, var(--green) 0%, var(--green-light) 35%, var(--green-mid) 70%, var(--green) 100%);
  }
</style>
</head>
<body>

<section class="card card--brand" aria-label="Card front">
  <div class="brand-name"><span class="brand-dot" aria-hidden="true"></span>Maplow Hearing Center</div>
</section>

<section class="card card--contact" aria-label="Card back">
  <div class="contact-top"></div>
  <div class="contact-logo">Maplow Hearing Center<span class="brand-dot" aria-hidden="true"></span></div>

  <p class="provider">Peter Mulvoy, Au.D. F/ISN</p>
  <ul class="details">
    <li>
      <svg viewBox="0 0 12 12" aria-hidden="true"><path d="M2.5 0.5 L4.5 0.5 L5 3.2 L3.8 4.2 C4.4 5.6 6.4 7.6 7.8 8.2 L8.8 7 L11.5 7.5 L11.5 9.5 C11.5 10.6 10.6 11.5 9.5 11.5 C4.5 11.2 0.8 7.5 0.5 2.5 C0.5 1.4 1.4 0.5 2.5 0.5 Z"/></svg>
      (555) 318-6042
    </li>
    <li>
      <svg viewBox="0 0 12 12" aria-hidden="true"><path d="M0.5 2 H11.5 V10 H0.5 Z M1.5 3 V3.4 L6 6.4 L10.5 3.4 V3 Z"/></svg>
      <span>maplow<span class="accent">hearing</span>@postvale.net</span>
    </li>
    <li>
      <svg viewBox="0 0 12 12" aria-hidden="true"><path d="M6 0.5 A5.5 5.5 0 1 0 6 11.5 A5.5 5.5 0 1 0 6 0.5 Z M6 1.8 C6.8 2.6 7.3 4 7.4 5.4 H4.6 C4.7 4 5.2 2.6 6 1.8 Z M4.6 6.6 H7.4 C7.3 8 6.8 9.4 6 10.2 C5.2 9.4 4.7 8 4.6 6.6 Z M1.8 5.4 C2 3.9 3 2.6 4.2 2.1 C3.7 3 3.4 4.2 3.4 5.4 Z M1.8 6.6 H3.4 C3.4 7.8 3.7 9 4.2 9.9 C3 9.4 2 8.1 1.8 6.6 Z M8.6 5.4 C8.6 4.2 8.3 3 7.8 2.1 C9 2.6 10 3.9 10.2 5.4 Z M8.6 6.6 H10.2 C10 8.1 9 9.4 7.8 9.9 C8.3 9 8.6 7.8 8.6 6.6 Z"/></svg>
      <span>www.maplow<span class="accent">hearing</span>.com</span>
    </li>
  </ul>

  <address class="address">
    87 W. Linden<br>
    Ave. Brookmere<br>
    OH 45190
  </address>

  <div class="contact-stripe"></div>
  <div class="contact-band"></div>
</section>

</body>
</html>
```